Experienced Home remodel service

I'm a home remodeler. I want a catch phrase that clearly describes viewers what kind of work I'm in like the purple phrase on my rough draft idea. I need my website, phone, logo, slogan included. The picture is of my daughter. I want her on it. Be cool if something could be added to her picture like a hard hat or tool belt ect and her picture cut out/background removed. Some kind of background other than plain white for whole picture. I added extra pics of her so pick one

Target Market(s)

Home owners between 30-60

Industry/Entity Type

Home renovation/remodel

Colors

Designer to choose colors to be used in the design.

Requirements
Must have
• Daughters picture incorporated. Logo, phone, website address, slogan,
Nice to have
• See a hardhat or tool belt added to one of my daughters pictures that is chosen to use by designer

```html
<!DOCTYPE html>
<html lang="en">
<head>
<meta charset="utf-8">
<title>Harlow Home Solutions – Billboard</title>
<link rel="stylesheet" href="https://fonts.googleapis.com/css2?family=Bebas+Neue&family=Saira+Condensed:wght@700&family=Cabin:wght@500&display=swap">
<style>
  :root {
    --stage: #333333;
    --paper: #ffffff;
    --ink: #0a0a0a;
    --violet: #8a55ee;
    --night: #050505;
    --photo-dark: #1c1a20;
    --photo-light: #cdb8d6;
  }
  * { margin: 0; padding: 0; box-sizing: border-box; }
  html, body {
    width: 1130px; height: 1200px; overflow: hidden;
    background: var(--stage);
  }
  .billboard {
    position: absolute; left: 0; top: 331px;
    width: 1130px; height: 538px;
    background: var(--paper);
    overflow: hidden;
  }
  .billboard__shapes { position: absolute; inset: 0; }
  .photo {
    position: absolute; left: 690px; top: 0;
    width: 440px; height: 418px;
    background: linear-gradient(180deg, var(--photo-dark) 0%, var(--photo-light) 100%);
  }
  .headline {
    position: absolute; left: 31px; top: 28px;
    font-family: "Bebas Neue", "Arial Narrow", sans-serif;
    font-size: 116px; line-height: 104px;
    color: var(--ink); letter-spacing: 2px;
  }
  .headline__accent { color: var(--violet); }
  .brand {
    position: absolute; left: 32px; top: 370px;
    display: flex; align-items: center; gap: 34px;
    color: var(--paper);
  }
  .brand__mark { width: 62px; height: 62px; background: var(--paper); }
  .brand__name, .brand__slogan {
    font-family: "Saira Condensed", "Arial Narrow", sans-serif;
    font-weight: 700; letter-spacing: 1.5px; line-height: 1;
  }
  .brand__name { font-size: 37px; }
  .brand__slogan { font-size: 31px; margin-top: 4px; }
  .website {
    position: absolute; left: 37px; top: 476px;
    font-family: "Cabin", Arial, sans-serif; font-weight: 500;
    font-size: 33px; color: var(--paper); letter-spacing: 0.5px;
  }
  .phone {
    position: absolute; left: 608px; top: 446px;
    display: flex; align-items: center; gap: 12px;
  }
  .phone__icon { width: 52px; height: 52px; }
  .phone__number {
    font-family: "Bebas Neue", "Arial Narrow", sans-serif;
    font-size: 84px; line-height: 1; color: var(--ink);
  }
</style>
</head>
<body>
  <main class="billboard">
    <svg class="billboard__shapes" width="1130" height="538" viewBox="0 0 1130 538">
      <polygon class="band band--dark" points="0,354 665,354 568,463 0,463" fill="var(--night)"/>
      <polygon class="band band--violet" points="0,463 568,463 500,538 0,538" fill="var(--violet)"/>
      <g role="img" aria-label="Large purple claw hammer graphic behind the photo">
        <polygon points="500,115 640,0 960,0 960,250 700,250" fill="var(--violet)"/>
      </g>
    </svg>

    <div class="photo" role="img" aria-label="Cut-out photo of the owner's daughter in a hard hat holding a hammer, on a black background"></div>

    <h1 class="headline">
      <span class="headline__accent">For All</span><br>
      <span class="headline__accent">Your</span> Home<br>
      Remodel Needs
    </h1>

    <div class="brand">
      <span class="brand__mark"></span>
      <div>
        <div class="brand__name">HARLOW HOME SOLUTIONS</div>
        <div class="brand__slogan">BUILD-REPAIR-REPLACE</div>
      </div>
    </div>

    <div class="website">HarlowHomeSolutions.com</div>

    <div class="phone">
      <svg class="phone__icon" viewBox="0 0 24 24" aria-hidden="true">
        <path fill="var(--ink)" d="M6.6 10.8c1.4 2.8 3.8 5.1 6.6 6.6l2.2-2.2c.3-.3.7-.4 1-.2 1.1.4 2.3.6 3.6.6.6 0 1 .4 1 1V20c0 .6-.4 1-1 1C10.6 21 3 13.4 3 4c0-.6.4-1 1-1h3.5c.6 0 1 .4 1 1 0 1.3.2 2.5.6 3.6.1.3 0 .7-.2 1l-2.3 2.2z"/>
        <path fill="none" stroke="var(--ink)" stroke-width="1.6" stroke-linecap="round" d="M14.5 3.5a6 6 0 0 1 6 6M14.5 6.5a3 3 0 0 1 3 3"/>
      </svg>
      <span class="phone__number">555-0148-2736</span>
    </div>
  </main>
</body>
</html>
```